Oakhaven Construction Need an information and interactive website with client portal. We have ou

Need to have a client log in screen for work orders and estimate requests.
Nice informational landing page.

Oakhaven is a full service general contractor servicing apartment complexes;
maintenance of grounds and apartments - remodeling and construction.

Design Specifics: We are pretty open here. Some good examples are
www.marrowpeakbuilders.com , tovelresidence.com and www.quillbyworksite.com

For the site we need:
Homepage - to explain services
Roofing page
Apartment Page
Client Portal - where clients can set up accounts to set up work/estimate request that will be routed to our email

--Will need coding, plan to host site on Wordpress

Target Market(s)

Multi family, Residential and commercial clients

Industry/Entity Type

Construction

Coding

Coded - Design and coding required

Number of Pages Required

3 page

Font styles to use
Serif

Requirements
Must have
• Client portal
Nice to have
• Not sure. please advise

```html
<!DOCTYPE html>
<html lang="en">
<head>
<meta charset="utf-8">
<title>Oakhaven Construction</title>
<link href="https://fonts.googleapis.com/css2?family=Roboto:wght@400;500;700&family=Lato:ital,wght@0,400;0,700;1,400;1,700&display=swap" rel="stylesheet">
<style>
:root{
  --red:#c0171b;
  --red-dark:#9e1014;
  --ink:#1b1b1b;
  --dark:#222325;
  --darker:#161617;
  --paper:#f1efec;
  --white:#ffffff;
  --muted:#555555;
  --line:#d6d3cf;
}
*{box-sizing:border-box;margin:0;padding:0}
html,body{width:1200px;height:3315px;overflow:hidden}
body{position:relative;background:var(--paper);font-family:"Lato",sans-serif;color:var(--ink)}
.abs{position:absolute}
.heading{font-family:"Roboto",sans-serif;font-weight:700;color:var(--ink)}
.heading em{font-style:normal;color:var(--red)}

/* top bar */
.topbar{left:540px;top:0;width:660px;height:36px;background:var(--red);display:flex;align-items:center;color:var(--white);font-size:15px}
.topbar .item{display:flex;align-items:center;gap:8px;padding:0 22px}
.topbar .login{margin-left:auto;background:var(--darker);height:36px;padding:0 24px;font-weight:700}
/* header */
.header{left:0;top:0;width:1200px;height:133px;background:var(--white)}
.brand{left:98px;top:52px;display:flex;align-items:center;gap:12px;font-family:"Roboto",sans-serif;font-weight:700;font-size:27px;color:var(--red)}
.brand .mark{width:30px;height:30px;background:var(--red)}
.nav{right:98px;top:72px;display:flex;gap:40px;font-family:"Roboto",sans-serif;font-size:14px;color:#333}
.nav .on{color:var(--red);font-weight:700}
/* hero */
.hero{left:0;top:133px;width:1200px;height:600px;background:
  radial-gradient(ellipse 260px 200px at 230px 170px,rgba(224,130,40,.55),transparent 70%),
  radial-gradient(ellipse 420px 380px at 340px 420px,rgba(246,246,246,.95),transparent 75%),
  linear-gradient(120deg,#f4f4f2 0%,#dfe2e3 40%,#b9bfc3 75%,#a8aeb2 100%)}
.hero-caption{left:0;top:648px;width:1200px;height:85px;background:rgba(20,20,20,.88);display:flex;align-items:center;justify-content:center;color:var(--white);font-family:"Roboto",sans-serif;font-weight:500;font-size:26px}
/* about */
.about-band{left:0;top:733px;width:1200px;height:345px;background:var(--white)}
.about-img{left:100px;top:773px;width:327px;height:261px;background:linear-gradient(160deg,#5f9ad6 0%,#a9c6e3 50%,#cfc9bd 100%);border-top:4px solid var(--red);border-left:4px solid var(--red)}
.about{left:469px;top:773px;width:632px}
.about h2{font-size:34px;display:flex;align-items:center;gap:14px}
.rule{display:inline-block;width:90px;height:4px;background:linear-gradient(90deg,#444,transparent)}
.about .lead{margin-top:20px;font-weight:700;font-size:15.5px}
.about p.body{margin-top:12px;font-size:14px;line-height:23px;color:#333}
.btn{display:inline-block;background:var(--red);color:var(--white);font-family:"Roboto",sans-serif;font-weight:700;font-size:14px;padding:10px 24px}
.btn-outline{display:inline-block;border:1.5px solid var(--white);color:var(--white);font-family:"Roboto",sans-serif;font-weight:700;font-size:14px;padding:8px 20px}
/* split */
.split-left{left:0;top:1078px;width:600px;height:327px;background:linear-gradient(135deg,#c9191d,#a71216)}
.split-right{left:600px;top:1078px;width:600px;height:327px;background:linear-gradient(135deg,#2a2b2d,#111)}
.split h3{font-family:"Roboto",sans-serif;font-weight:500;font-size:28px;color:var(--white);display:flex;align-items:center;gap:14px}
.split p{margin-top:16px;font-size:13.5px;line-height:23px;color:var(--white)}
.emblem{left:503px;top:1158px;width:194px;height:194px;border-radius:50%;background:var(--white);border:12px solid #2b2b2b;display:flex;align-items:center;justify-content:center;font-family:"Roboto",sans-serif;font-weight:700;font-size:21px;color:var(--red);text-align:center;line-height:24px}
/* services */
.sec-title{left:0;width:1200px;display:flex;justify-content:center;align-items:center;gap:20px;font-size:32px}
.sec-title .rule{width:110px;background:linear-gradient(90deg,transparent,#444)}
.sec-title .rule.r{background:linear-gradient(90deg,#444,transparent)}
.services-intro{left:130px;top:1500px;width:940px;text-align:center;font-size:13.5px;line-height:22px;color:#333}
.card{top:1562px;width:238px;height:190px;border:4px solid var(--red)}
.card .ico{position:absolute;left:50%;bottom:-4px;transform:translateX(-50%);width:58px;height:40px;background:var(--red);border-radius:29px 29px 0 0;display:flex;align-items:center;justify-content:center}
.card-label{top:1770px;width:238px;text-align:center;font-family:"Roboto",sans-serif;font-weight:500;font-size:17px}
.arrow{top:1645px;width:26px;height:26px;border-radius:50%;background:var(--white);border:1px solid var(--line);display:flex;align-items:center;justify-content:center}
/* cta */
.cta{left:0;top:1834px;width:1200px;height:128px;background:linear-gradient(90deg,#1c1d1f,#2d2f31 60%,#1c1d1f)}
.cta p{position:absolute;left:100px;top:40px;color:var(--white);font-family:"Roboto",sans-serif;font-weight:500;font-size:18px;line-height:26px}
.cta .btn{position:absolute;left:928px;top:45px;padding:11px 20px;font-size:15px}
/* testimonials */
.testi{left:140px;top:2606px;width:920px;text-align:center;font-style:italic;font-size:13.5px;line-height:26px;color:#333}
.testi-name{left:0;top:2690px;width:1200px;text-align:center;font-style:italic;font-weight:700;font-size:15px}
.avatar{top:2745px;width:72px;height:72px;border:4px solid #bdbdbd;background:linear-gradient(#e5e5e5,#bcbcbc)}
.avatar.on{border-color:var(--red)}
/* partners */
.partners{left:0;top:2862px;width:1200px;height:102px;background:#e8e8e8}
.partners-label{left:0;top:2862px;width:265px;height:102px;background:var(--red);color:var(--white);font-family:"Roboto",sans-serif;font-weight:700;font-size:27px;line-height:28px;padding:22px 0 0 98px}
.badge{top:2886px;height:54px;background:#9a9a9a}
/* footer */
.footer{left:0;top:2964px;width:1200px;height:302px;background:var(--dark)}
.footer-red{left:0;top:2964px;width:1200px;height:302px}
.footer-title{font-family:"Roboto",sans-serif;font-weight:700;font-size:20px;color:var(--white)}
.footer-line{width:260px;height:1px;background:#4a4a4a;margin-top:10px}
.f-list{list-style:none;margin-top:16px;font-size:13.5px;color:#ddd}
.f-list li{display:flex;align-items:flex-start;gap:14px;margin-bottom:11px;line-height:20px}
.links li{margin-bottom:7px}
.foot-brand{left:868px;top:3088px;display:flex;align-items:center;gap:10px;font-family:"Roboto",sans-serif;font-weight:700;font-size:22px;color:var(--white)}
.foot-brand .mark{width:20px;height:20px;background:var(--white)}
.social{top:3163px;display:flex;gap:8px;left:912px}
.social span{width:22px;height:22px;border-radius:50%;background:#1f5fa8}
.copy{left:0;top:3266px;width:1200px;height:49px;background:var(--darker);color:#ccc;font-size:13.5px;display:flex;align-items:center;justify-content:center}
.totop{left:1034px;top:3266px;width:100px;height:49px;background:#2c2c2e;clip-path:polygon(20% 0,80% 0,100% 100%,0 100%);display:flex;align-items:center;justify-content:center}
</style>
</head>
<body>

<header>
  <div class="abs header"></div>
  <div class="abs brand"><span class="mark"></span>Oakhaven Construction</div>
  <div class="abs topbar">
    <span class="item">
      <svg width="14" height="14" viewBox="0 0 24 24"><path fill="#fff" d="M6.6 10.8a15 15 0 006.6 6.6l2.2-2.2c.3-.3.7-.4 1-.2 1.1.4 2.3.6 3.6.6.6 0 1 .4 1 1V20c0 .6-.4 1-1 1A17 17 0 013 4c0-.6.4-1 1-1h3.5c.6 0 1 .4 1 1 0 1.3.2 2.5.6 3.6.1.3 0 .7-.2 1z"/></svg>
      +123.456.7890</span>
    <span class="item">
      <svg width="15" height="12" viewBox="0 0 24 18"><rect x="1" y="1" width="22" height="16" fill="none" stroke="#fff" stroke-width="2"/><path d="M1 1l11 9 11-9" fill="none" stroke="#fff" stroke-width="2"/></svg>
      info@oakhavenconstruction.com</span>
    <span class="item login">
      <svg width="13" height="13" viewBox="0 0 24 24"><path fill="#fff" d="M10 5l7 7-7 7v-4H2V9h8zM14 2h8v20h-8v-2h6V4h-6z"/></svg>
      Login</span>
  </div>
  <nav class="abs nav">
    <span class="on">Home</span><span>About</span><span>Services</span><span>Roofing</span><span>Apartment</span><span>Client Portal</span><span>Contact Us</span>
  </nav>
</header>

<section>
  <div class="abs hero" role="img" aria-label="Photo of two builders in orange hard hats reviewing a large blueprint on a bright glass balcony"></div>
  <div class="abs hero-caption">Multifamily &amp; Commercial Renovation Contractors</div>
</section>

<section>
  <div class="abs about-band"></div>
  <div class="abs about-img" role="img" aria-label="Photo of an engineer and a worker reviewing plans outdoors"></div>
  <div class="abs about">
    <h2 class="heading">About <em>Us</em><span class="rule"></span></h2>
    <p class="lead">Neque porro quisquam est, qui dolorem ipsum quia dolor sit amet, consectetur, adipisci</p>
    <p class="body">Lorem ipsum dolor sit amet, consectetur adipiscing elit, sed do eiusmod tempor incididunt ut labore et dolore magna aliqua. Ut enim ad minim veniam, quis nostrud exercitation ullamco laboris nisi ut aliquip ex ea commodo consequat. Duis aute irure dolor in reprehenderit in voluptate velit esse cillum dolore eu fugiat nulla pariatur. Excepteur sint occaecat cupidatat non proident, sunt in culpa qui officia deserunt mollit anim id est laborum</p>
    <span class="btn" style="margin-top:16px">Read More</span>
  </div>
</section>

<section class="split">
  <div class="abs split-left"></div>
  <div class="abs split-right"></div>
  <div class="abs" style="left:100px;top:1115px;width:370px">
    <h3>
      <svg width="52" height="34" viewBox="0 0 52 34"><path d="M2 22L26 4l24 18" fill="none" stroke="#fff" stroke-width="4"/><rect x="6" y="2" width="6" height="12" fill="#fff"/><rect x="10" y="26" width="32" height="4" fill="#fff"/></svg>
      Roofing</h3>
    <p>Lorem ipsum dolor sit amet, consectetur adipiscing elit, sed do eiusmod tempor incididunt ut labore et dolore magna aliqua. Ut enim ad minim veniam, quis nostrud exercitation ullamco laboris nisi ut aliquip ex ea commodo consequat. Duis aute irure dolor in reprehenderit in voluptate velit esse cillum dolore eu fugiat nulla pariatur. Excepteur sint occaecat</p>
    <span class="btn-outline" style="margin-top:16px">Read More</span>
  </div>
  <div class="abs" style="left:730px;top:1115px;width:370px;text-align:right">
    <h3 style="justify-content:flex-end">Apartment
      <svg width="30" height="38" viewBox="0 0 30 38"><rect x="3" y="2" width="24" height="34" fill="none" stroke="#fff" stroke-width="3"/><g fill="#fff"><rect x="8" y="7" width="4" height="4"/><rect x="18" y="7" width="4" height="4"/><rect x="8" y="15" width="4" height="4"/><rect x="18" y="15" width="4" height="4"/><rect x="8" y="23" width="4" height="4"/><rect x="18" y="23" width="4" height="4"/></g></svg></h3>
    <p>Lorem ipsum dolor sit amet, consectetur adipiscing elit, sed do eiusmod tempor incididunt ut labore et dolore magna aliqua. Ut enim ad minim veniam, quis nostrud exercitation ullamco laboris nisi ut aliquip ex ea commodo consequat. Duis aute irure dolor in reprehenderit in voluptate velit esse cillum dolore eu fugiat nulla pariatur. Excepteur sint occaecat</p>
    <span class="btn-outline" style="margin-top:16px">Read More</span>
  </div>
  <div class="abs emblem">Oakhaven<br>Construction</div>
</section>

<section>
  <h2 class="abs sec-title heading" style="top:1442px"><span class="rule"></span><span>Our <em>Services</em></span><span class="rule r"></span></h2>
  <p class="abs services-intro">Sed ut perspiciatis unde omnis iste natus error sit voluptatem accusantium doloremque laudantium, totam rem aperiam, eaque ipsa quae ab illo inventore veritatis et quasi architecto beatae vitae dicta sunt explicabo. Nemo enim ipsam voluptatem quia voluptas sit</p>
  <div class="abs arrow" style="left:50px"><svg width="8" height="10" viewBox="0 0 8 10"><path d="M6 1L2 5l4 4" fill="none" stroke="#333" stroke-width="1.6"/></svg></div>
  <div class="abs arrow" style="left:1124px"><svg width="8" height="10" viewBox="0 0 8 10"><path d="M2 1l4 4-4 4" fill="none" stroke="#333" stroke-width="1.6"/></svg></div>

  <div class="abs card" style="left:100px;background:linear-gradient(160deg,#d9a866,#8a5a2c)" role="img" aria-label="Photo of a builder on a new timber frame">
    <span class="ico"><svg width="22" height="18" viewBox="0 0 22 18"><path d="M1 9l10-8 10 8M4 8v9h14V8" fill="none" stroke="#fff" stroke-width="2"/></svg></span></div>
  <div class="abs card" style="left:354px;background:linear-gradient(160deg,#b07a4f,#6e4426)" role="img" aria-label="Photo of a worker fitting kitchen cabinets">
    <span class="ico"><svg width="20" height="20" viewBox="0 0 20 20"><path d="M3 17L15 5M5 3l12 12" stroke="#fff" stroke-width="3"/></svg></span></div>
  <div class="abs card" style="left:608px;background:linear-gradient(160deg,#d8c59c,#8d7650)" role="img" aria-label="Photo of a restored arched interior">
    <span class="ico"><svg width="22" height="18" viewBox="0 0 22 18"><path d="M2 17V8l9-6 9 6v9z" fill="#fff"/></svg></span></div>
  <div class="abs card" style="left:862px;background:linear-gradient(160deg,#dfe3e6,#8e9499)" role="img" aria-label="Photo of an empty commercial interior under construction">
    <span class="ico"><svg width="18" height="18" viewBox="0 0 18 18"><path d="M3 3l12 12M15 3L3 15" stroke="#fff" stroke-width="3.5"/></svg></span></div>
  <div class="abs card-label" style="left:100px">New Construction</div>
  <div class="abs card-label" style="left:354px">Remodeling</div>
  <div class="abs card-label" style="left:608px">Restoration</div>
  <div class="abs card-label" style="left:862px">Phased Construction</div>
</section>

<section class="abs cta">
  <p>For more information about our Oakhaven projects &amp; services or to<br>receive a comprehensive estimate on your upcoming project</p>
  <span class="btn">Request A Quote</span>
</section>

<section>
  <h2 class="abs sec-title heading" style="top:1999px"><span class="rule"></span><span>Project <em>Gallery</em></span><span class="rule r"></span></h2>
  <div class="abs" style="left:117px;top:2068px;width:310px;height:186px;background:linear-gradient(160deg,#e3c9a4,#9a7149)" role="img" aria-label="Photo of workers fitting a kitchen"></div>
  <div class="abs" style="left:444px;top:2068px;width:310px;height:186px;background:linear-gradient(180deg,#4d8fd0,#e8eef2 60%,#3aa7c4)" role="img" aria-label="Photo of a white apartment building with a pool"></div>
  <div class="abs" style="left:771px;top:2068px;width:312px;height:392px;background:linear-gradient(180deg,#f1c15a,#d1822a 60%,#5a3414)" role="img" aria-label="Photo of builders silhouetted against a sunset crane"></div>
  <div class="abs" style="left:117px;top:2272px;width:310px;height:188px;background:linear-gradient(160deg,#f2f2f2,#a3a3a3)" role="img" aria-label="Photo of a modern white kitchen"></div>
  <div class="abs" style="left:444px;top:2272px;width:310px;height:188px;background:linear-gradient(160deg,#d9dde1,#9fa7ae);border:3px solid #3f6fbf" role="img" aria-label="Photo of a builder in a hard hat, with zoom overlay">
    <svg style="position:absolute;left:135px;top:72px" width="40" height="40" viewBox="0 0 40 40"><circle cx="16" cy="16" r="11" fill="none" stroke="#222" stroke-width="3"/><path d="M24 24l12 12M16 10v12M10 16h12" stroke="#222" stroke-width="3"/></svg>
  </div>
</section>

<section>
  <div class="abs" style="left:0;top:2508px;width:1200px;height:354px;background:var(--white)"></div>
  <h2 class="abs sec-title heading" style="top:2541px"><span class="rule"></span><span>Client <em>Testimonials</em></span><span class="rule r"></span></h2>
  <p class="abs testi">Lorem ipsum dolor sit amet, consectetur adipiscing elit, sed do eiusmod tempor incididunt ut labore et dolore magna aliqua. Ut enim veniam, quis nostrud exercitation ullamco laboris nisi ut aliquip ex ea commodo consequat. Duis aute irure dolor in reprehenderit in voluptate velit esse cillum dolore eu fugiat nulla pariatur. Excepteur sint occaecat cupidatat non proident, sunt in culpa qui officia .</p>
  <p class="abs testi-name">- Sconsectetur adipiscing</p>
  <div class="abs avatar" style="left:466px" role="img" aria-label="Client portrait"></div>
  <div class="abs avatar on" style="left:564px" role="img" aria-label="Client portrait"></div>
  <div class="abs avatar" style="left:662px" role="img" aria-label="Client portrait"></div>
</section>

<section>
  <div class="abs partners"></div>
  <div class="abs partners-label">OUR<br>PARTNERS</div>
  <svg class="abs" style="left:278px;top:2903px" width="10" height="18" viewBox="0 0 10 18"><path d="M8 2L2 9l6 7" fill="none" stroke="#888" stroke-width="2"/></svg>
  <svg class="abs" style="left:1090px;top:2903px" width="10" height="18" viewBox="0 0 10 18"><path d="M2 2l6 7-6 7" fill="none" stroke="#888" stroke-width="2"/></svg>
  <div class="abs badge" style="left:326px;top:2898px;width:134px;height:30px"></div>
  <div class="abs badge" style="left:520px;width:54px;border-radius:50%"></div>
  <div class="abs badge" style="left:658px;width:66px;border-radius:50%"></div>
  <div class="abs badge" style="left:800px;width:80px;height:50px"></div>
  <div class="abs badge" style="left:950px;top:2895px;width:98px;height:36px;border-radius:18px"></div>
</section>

<footer>
  <div class="abs footer"></div>
  <svg class="abs footer-red" viewBox="0 0 1200 302" preserveAspectRatio="none"><polygon points="782,0 1200,0 1200,302 840,302" fill="#c0171b"/></svg>
  <div class="abs" style="left:142px;top:3012px">
    <h4 class="footer-title">Contact Address</h4><div class="footer-line"></div>
    <ul class="f-list">
      <li><svg width="12" height="16" viewBox="0 0 12 16"><path d="M6 0a6 6 0 016 6c0 4-6 10-6 10S0 10 0 6a6 6 0 016-6z" fill="#fff"/><circle cx="6" cy="6" r="2" fill="#222"/></svg>Lorem ipsum dolor sitamet, consectetuer<br>adipiscing sed diammy.</li>
      <li><svg width="14" height="14" viewBox="0 0 24 24"><path fill="#fff" d="M6.6 10.8a15 15 0 006.6 6.6l2.2-2.2c.3-.3.7-.4 1-.2 1.1.4 2.3.6 3.6.6.6 0 1 .4 1 1V20c0 .6-.4 1-1 1A17 17 0 013 4c0-.6.4-1 1-1h3.5c.6 0 1 .4 1 1 0 1.3.2 2.5.6 3.6.1.3 0 .7-.2 1z"/></svg>+123.456.7890</li>
      <li><svg width="14" height="14" viewBox="0 0 14 14"><rect x="3" y="0" width="8" height="4" fill="#fff"/><rect x="0" y="5" width="14" height="6" fill="#fff"/><rect x="3" y="9" width="8" height="5" fill="#fff"/></svg>+123.456.7890</li>
      <li><svg width="14" height="11" viewBox="0 0 24 18"><rect x="1" y="1" width="22" height="16" fill="#fff"/><path d="M1 1l11 9 11-9" fill="none" stroke="#222" stroke-width="2"/></svg>info@oakhavenconstruction.com</li>
    </ul>
  </div>
  <div class="abs" style="left:516px;top:3012px">
    <h4 class="footer-title">Quick Links</h4><div class="footer-line" style="width:130px"></div>
    <ul class="f-list links">
      <li>› &nbsp;Home</li><li>› &nbsp;About Us</li><li>› &nbsp;Services</li><li>› &nbsp;Roofing</li><li>› &nbsp;Apartment</li><li>› &nbsp;Client Portal</li><li>› &nbsp;Contact Us</li>
    </ul>
  </div>
  <div class="abs foot-brand"><span class="mark"></span>Oakhaven</div>
  <div class="abs social"><span></span><span></span><span></span><span style="background:#d9342b"></span></div>
  <div class="abs copy">Copyright © 2016 Oakhaven Construction . All Right Reserved.</div>
  <div class="abs totop"><svg width="16" height="10" viewBox="0 0 16 10"><path d="M2 8l6-6 6 6" fill="none" stroke="#fff" stroke-width="2"/></svg></div>
</footer>

</body>
</html>
```